Business card for a gourmet fruit and vegetable retail store

Please design a business card for our boutique gourmet fruit and vegetable food store using attached logo design, with the colour options of white, black and lime green. We would like it to be unique and classic, with a large image of the logo on the back of the business card, and the business card details plus a design on the front.

Target Market(s)

High income earners in an affluent Melbourne suburb who value high quality products and done mind paying for it

Industry/Entity Type

Retail

Contact Information for Business Card

Business name: Haddleby's Fine Food Merchant
Address: 27 Quillmont Rd, Tarnvale VIC 3188
Name: TBC
Position Title: Director
Phone Number: TBC
Mobile: TBC

Business name is: Haddleby's Fine Food Merchant. Please allow space for us to fill in the business address, contact number, person's name, position Title and mobile number.

Colors
acd036

Requirements
Must have
• The logo must have our business logo on the back, and our business details and contact details on the front. It must include the colours of white, black and lime green
Nice to have
• It can have different background colours on the front and on the back.
Should not have
• It should not have any other colours aside from white, black and lime green

```html
<!DOCTYPE html>
<html lang="en">
<head>
<meta charset="utf-8">
<title>Haddleby's Fine Food Merchant – Business Card</title>
<link rel="stylesheet" href="https://fonts.googleapis.com/css2?family=Oswald:wght@500&family=Open+Sans:wght@400;600&display=swap">
<style>
  :root {
    --lime: #acd036;
    --ink: #1b1b1b;
    --paper: #ffffff;
    --text-grey: #555555;
    --rule-grey: #666666;
    --backdrop: #e9e6e1;
  }
  * { margin: 0; padding: 0; box-sizing: border-box; }
  html, body { width: 1200px; height: 1000px; overflow: hidden; }
  body {
    position: relative;
    background: var(--backdrop);
    font-family: "Open Sans", Arial, sans-serif;
  }
  .card {
    position: absolute;
    left: 266px;
    width: 666px;
    height: 397px;
    border-radius: 28px;
    overflow: hidden;
  }
  .card--back { top: 74px; background: var(--ink); }
  .card--front { top: 533px; background: var(--paper); }

  .brand-mark {
    position: absolute;
    left: 195px; top: 61px;
    width: 276px; height: 276px;
    border: 2px solid var(--lime);
    border-radius: 50%;
    display: flex; align-items: center; justify-content: center;
  }
  .brand-name {
    font-family: "Open Sans", Arial, sans-serif;
    font-weight: 600;
    font-size: 36px;
    color: var(--lime);
    letter-spacing: 1px;
  }

  .person {
    position: absolute;
    right: 372px; top: 158px;
    text-align: right;
  }
  .person__name {
    font-family: "Oswald", "Arial Narrow", sans-serif;
    font-weight: 500;
    font-size: 25px;
    line-height: 30px;
    color: var(--lime);
    letter-spacing: 0.3px;
  }
  .person__title {
    font-size: 16px;
    line-height: 22px;
    color: var(--text-grey);
  }
  .divider {
    position: absolute;
    left: 318px; top: 167px;
    width: 2px; height: 59px;
    background: var(--rule-grey);
  }
  .contact {
    position: absolute;
    left: 346px; top: 163px;
    list-style: none;
  }
  .contact li {
    display: flex; align-items: center;
    font-size: 16px; line-height: 22.5px;
    color: var(--text-grey);
  }
  .contact svg { width: 13px; height: 13px; margin-right: 8px; fill: var(--lime); }
  .address {
    position: absolute;
    left: 0; right: 0; top: 347px;
    text-align: center;
    font-size: 16px;
    color: var(--text-grey);
  }
  .address__company { color: var(--lime); font-weight: 600; }
</style>
</head>
<body>
  <section class="card card--back" aria-label="Card back">
    <div class="brand-mark">
      <span class="brand-name">Haddleby's</span>
    </div>
  </section>

  <section class="card card--front" aria-label="Card front">
    <div class="person">
      <p class="person__name">MARLA J. PENHALLOW</p>
      <p class="person__title">Chief Executive Officer</p>
    </div>
    <div class="divider"></div>
    <ul class="contact">
      <li>
        <svg viewBox="0 0 16 16" aria-hidden="true"><path d="M1 6c0-2 3-4 7-4s7 2 7 4l-1 1-3-1V5C10 4.5 6 4.5 5 5v1L2 7zM4 8l1-2h6l1 2 2 2v4H2v-4zm4 1.5a2 2 0 1 0 0 4 2 2 0 0 0 0-4z"/></svg>
        00 000 000 000
      </li>
      <li>
        <svg viewBox="0 0 16 16" aria-hidden="true"><path d="M4.5 1h7a1 1 0 0 1 1 1v12a1 1 0 0 1-1 1h-7a1 1 0 0 1-1-1V2a1 1 0 0 1 1-1zm.6 1.6v9.4h5.8V2.6zM8 12.8a.7.7 0 1 0 0 1.4.7.7 0 0 0 0-1.4z"/></svg>
        00 000 000 000
      </li>
      <li>
        <svg viewBox="0 0 16 16" aria-hidden="true"><path d="M1 3h14v10H1zm1.5 1.3v.4L8 8.6l5.5-3.9v-.4zm0 2v5.4h11V6.3L8 10.2z"/></svg>
        info@haddlebysfinefood.com
      </li>
    </ul>
    <p class="address"><span class="address__company">Haddleby's Fine Food Merchant</span> 27 Quillmont Rd, Tarnvale VIC 3188</p>
  </section>
</body>
</html>
```